Northfield Builders Guild Business card

We are looking for a new business card design with photo included.
Our business is a nonprofit construction contractor membership organization. We offer business education, assist with business setup and licensing, provide safety training, and provide a member directory.
URL: www.brickwayguildnetwork.org
Color code:
CMYK: 0 cyan, 42 magenta, 100 yellow, 0 black for Print.
Hexidecimal: #FF9900
RGB: R 255; G 153; B 0

```html
<!DOCTYPE html>
<html lang="en">
<head>
<meta charset="utf-8">
<title>Northfield Builders Guild – Business Card</title>
<link href="https://fonts.googleapis.com/css2?family=Open+Sans:ital,wght@0,400;0,600;0,800;1,400&display=swap" rel="stylesheet">
<style>
  :root {
    --brand-orange: #ff9900;
    --ink: #2b2b2b;
    --text-grey: #555555;
    --card-white: #ffffff;
    --card-black: #161616;
    --stage: #e9e9e9;
    --photo-light: #f1f2f5;
    --photo-mid: #c6ccd8;
    --photo-navy: #2c4170;
  }
  * { box-sizing: border-box; margin: 0; padding: 0; }
  html, body { width: 1200px; height: 900px; overflow: hidden; }
  body {
    background: var(--stage);
    font-family: "Open Sans", Arial, sans-serif;
    display: flex;
    flex-direction: column;
    align-items: center;
    justify-content: center;
    gap: 50px;
  }
  .card {
    width: 640px;
    height: 366px;
    position: relative;
    overflow: hidden;
    box-shadow: 0 8px 24px rgba(0,0,0,0.18);
  }
  /* Front */
  .card-front { background: var(--card-white); }
  .wordmark {
    position: absolute;
    left: 40px;
    top: 34px;
    font-weight: 800;
    font-size: 30px;
    line-height: 1.05;
    color: var(--ink);
    text-transform: uppercase;
    letter-spacing: -0.5px;
  }
  .holder {
    position: absolute;
    left: 40px;
    top: 132px;
  }
  .holder-name {
    font-weight: 600;
    font-size: 21px;
    color: var(--brand-orange);
    text-transform: uppercase;
    letter-spacing: 0.2px;
  }
  .holder-title {
    font-style: italic;
    font-size: 14px;
    color: var(--text-grey);
    margin-top: 1px;
  }
  .address {
    position: absolute;
    left: 40px;
    top: 200px;
    font-size: 14px;
    line-height: 1.4;
    color: var(--text-grey);
  }
  .contact-list {
    position: absolute;
    left: 40px;
    top: 256px;
    list-style: none;
    font-size: 14px;
    line-height: 1.5;
    color: var(--text-grey);
  }
  .contact-list li { display: flex; align-items: center; gap: 7px; }
  .contact-list svg { width: 12px; height: 12px; flex: none; }
  .portrait {
    position: absolute;
    right: 0;
    bottom: 0;
    width: 290px;
    height: 250px;
    background: linear-gradient(180deg, var(--photo-light) 0%, var(--photo-mid) 50%, var(--photo-navy) 100%);
  }
  /* Back */
  .card-back {
    background: var(--card-black);
    display: flex;
    align-items: center;
    justify-content: center;
  }
  .wordmark-back {
    font-weight: 800;
    font-size: 44px;
    line-height: 1.05;
    color: var(--brand-orange);
    text-transform: uppercase;
    text-align: center;
    letter-spacing: -0.5px;
  }
</style>
</head>
<body>
  <section class="card card-front">
    <div class="wordmark">Northfield<br>Builders Guild</div>

    <div class="holder">
      <p class="holder-name">Daniel Reyes</p>
      <p class="holder-title">President</p>
    </div>

    <p class="address">2450 Alder Ridge Rd, Suite #210<br>Salem, OR 97301</p>

    <ul class="contact-list">
      <li>
        <svg viewBox="0 0 12 12" aria-hidden="true"><path fill="var(--brand-orange)" d="M2.4 0.6 4.2 2.7 3.2 4.1c.6 1.5 1.6 2.6 3 3.3l1.3-1.1 2.1 1.7-1 2.3C4.4 10.1 1 6.6.6 2Z"/></svg>
        (503) 555-0187
      </li>
      <li>
        <svg viewBox="0 0 12 12" aria-hidden="true"><rect x="0.5" y="2" width="11" height="8" fill="var(--brand-orange)"/><path d="M0.5 2 6 6.5 11.5 2" stroke="#fff" fill="none" stroke-width="1"/></svg>
        support@nbguild.org
      </li>
      <li>
        <svg viewBox="0 0 12 12" aria-hidden="true"><circle cx="6" cy="6" r="5.5" fill="var(--brand-orange)"/><path d="M0.5 6h11M6 0.5c-2.2 2.8-2.2 8.2 0 11M6 0.5c2.2 2.8 2.2 8.2 0 11" stroke="#fff" fill="none" stroke-width="0.8"/></svg>
        www.brickwayguildnetwork.org
      </li>
    </ul>

    <div class="portrait" role="img" aria-label="Portrait photo of the guild president in a navy blazer and white shirt"></div>
  </section>

  <section class="card card-back">
    <div class="wordmark-back">Northfield<br>Builders Guild</div>
  </section>
</body>
</html>
```